Webdesign Bestattung Helga Rothmaier
Zielgruppe
es handelt sich um ein Bestattungsunternehmen // Ziel des Unternehmens ist die Ansprache von Hinterbliebenen. Es sollen klare Informationen transportiert werden und schnelle Hilfe im Trauerfall angeboten werden.
Aufgabenstellung
- btte beachten -> der Name lautet jetzt 'Bestattung Helga Rothmaier'
-Seite soll einladen und nicht zu 'depressiv' sein
- berücksichtigen Sie bitte die KOntaktmöglichkeiten für die einzelnen Standort -> präsent platzieren
- ganz wenig schwarz & keine schwarzen Balken
- klare Informationen auf der Startseite
- schneller Zugang zu Kontaktmöglichkeiten
- Layout aufgelockert gern etwas geschwungenen Elemente
- Farbgebung Magenta & Gold / punktuell schwarz aber sehr dezent
- modern trotz des schweren Themas

```html
<!DOCTYPE html>
<html lang="de">
<head>
<meta charset="utf-8">
<title>Bestattung Helga Rothmaier</title>
<link href="https://fonts.googleapis.com/css2?family=Cormorant+Garamond:ital,wght@0,500;0,600;1,500;1,600&family=Inter:wght@400;500;600;700&display=swap" rel="stylesheet">
<style>
:root{
  --magenta:#d0164a;
  --magenta-dark:#a3143c;
  --magenta-soft:#fde9ee;
  --gold:#ee9a0c;
  --gold-light:#f5b02a;
  --green:#1aa766;
  --green-soft:#eefaf3;
  --ink:#2a2226;
  --muted:#6b6468;
  --line:#f0e6e9;
  --cream:#fffaf3;
  --blush:#fff6f7;
}
*{box-sizing:border-box;margin:0;padding:0}
html,body{width:1200px;height:3044px;overflow:hidden}
body{font-family:'Inter',sans-serif;color:var(--ink);background:#fff;font-size:13px}
.accent{font-family:'Cormorant Garamond',serif;font-style:italic;color:var(--magenta)}
.wrap{position:relative;width:1028px;margin:0 auto;height:100%}
section,header,footer{position:relative}
svg.i{width:14px;height:14px;fill:none;stroke:currentColor;stroke-width:2;stroke-linecap:round;stroke-linejoin:round;flex:none}
.btn{display:inline-flex;align-items:center;gap:8px;border-radius:30px;font-weight:600;text-decoration:none;white-space:nowrap}
.btn-magenta{background:linear-gradient(90deg,var(--magenta),var(--magenta-dark));color:#fff;box-shadow:0 6px 14px rgba(208,22,74,.25)}
.btn-gold{background:linear-gradient(90deg,var(--gold-light),var(--gold));color:#fff;box-shadow:0 6px 14px rgba(238,154,12,.25)}
.btn-chat{background:var(--green-soft);color:#167a4c;border:1px solid #cdeedd}
.btn-outline{border:1.5px solid var(--magenta);color:var(--magenta);background:#fff}

/* header */
.site-header{height:79px;border-bottom:1px solid var(--line)}
.brand{position:absolute;left:0;top:14px;display:flex;align-items:center;gap:12px}
.brand-dot{width:30px;height:30px;border-radius:50%;background:var(--magenta-soft)}
.brand-kicker{font-size:10px;color:var(--muted);line-height:1;margin-bottom:4px}
.brand-name{font-family:'Cormorant Garamond',serif;font-weight:600;font-size:20px;color:var(--magenta-dark);line-height:1;white-space:nowrap}
.brand-tag{font-size:10px;color:var(--muted);margin-top:4px;white-space:nowrap}
.nav{position:absolute;left:282px;top:32px;display:flex;gap:22px;font-size:12px;font-weight:500;white-space:nowrap}
.header-actions{position:absolute;right:0;top:22px;display:flex;gap:6px}
.header-actions .btn{height:34px;padding:0 13px;font-size:12px}

/* hero */
.hero{height:480px;background:linear-gradient(180deg,#fff 0%,var(--blush) 100%);border-bottom:1px solid #f6d6dd}
.badge{position:absolute;left:0;top:72px;display:flex;align-items:center;gap:6px;padding:5px 10px;border:1px solid #f3d9df;border-radius:20px;background:#fff;font-size:10px;color:var(--magenta)}
.hero h1{position:absolute;left:0;top:108px;width:520px;font-family:'Cormorant Garamond',serif;font-weight:600;font-size:45px;line-height:49px;letter-spacing:-.3px;white-space:nowrap}
.hero-lead{position:absolute;left:0;top:290px;width:470px;font-size:14px;line-height:27px;color:#403a3d}
.hero-actions{position:absolute;left:0;top:367px;display:flex;gap:14px}
.hero-actions .btn{height:42px;padding:0 20px;font-size:13px}
.hero-photo{position:absolute;left:531px;top:54px;width:497px;height:372px;border-radius:18px;background:linear-gradient(180deg,#33445a 0%,#8c8e92 45%,#d9b57a 58%,#6f6a66 80%,#3a3b40 100%);box-shadow:0 12px 30px rgba(0,0,0,.15)}
.reach-card{position:absolute;left:531px;top:344px;width:484px;height:102px;background:rgba(255,255,255,.94);border-radius:14px;box-shadow:0 10px 26px rgba(0,0,0,.1);padding:18px 18px}
.reach-top{display:flex;gap:12px;align-items:center}
.reach-ic{width:32px;height:32px;border-radius:50%;background:var(--magenta-soft);color:var(--magenta);display:flex;align-items:center;justify-content:center}
.reach-top b{display:block;font-size:12px}
.reach-top span{font-size:10px;color:var(--muted)}
.reach-places{display:flex;gap:10px;margin-top:16px;font-size:10px;font-weight:500}
.reach-places span{display:flex;align-items:center;gap:3px}
.reach-places svg{width:11px;height:11px;color:var(--magenta)}

/* locations */
.locations{height:451px}
.sec-title{font-family:'Cormorant Garamond',serif;font-weight:600;font-size:31px;line-height:34px}
.locations .sec-title{position:absolute;left:0;top:52px}
.rule{position:absolute;width:52px;height:3px;border-radius:2px;background:#f3a3b3}
.info-note{position:absolute;right:0;top:54px;width:497px;height:68px;border-radius:12px;background:var(--green-soft);border:1px solid #dcf2e6;display:flex;align-items:center;gap:14px;padding:0 16px;font-size:12px;line-height:21px}
.info-note .ic{width:32px;height:32px;border-radius:50%;background:#d8f3e4;color:var(--green);display:flex;align-items:center;justify-content:center}
.info-note b{color:#167a4c}
.loc-grid{position:absolute;left:0;top:156px;display:flex;gap:18px}
.loc-card{width:191px;height:242px;background:#fff;border-radius:14px;box-shadow:0 4px 18px rgba(160,40,70,.08);text-align:center;padding-top:20px}
.loc-ic{width:52px;height:52px;margin:0 auto;border-radius:50%;background:var(--magenta-soft);color:var(--magenta);display:flex;align-items:center;justify-content:center}
.loc-ic svg{width:24px;height:24px}
.loc-card h3{font-family:'Cormorant Garamond',serif;font-weight:600;font-size:18px;margin-top:14px}
.loc-card p{font-size:10px;line-height:16px;color:var(--muted);margin-top:7px}
.loc-card .btn{height:32px;font-size:11px;margin-top:14px;justify-content:center;width:150px;padding:0}
.route{display:flex;justify-content:center;align-items:center;gap:4px;margin-top:10px;font-size:10px;color:var(--gold);font-weight:500}
.route svg{width:11px;height:11px}

/* about */
.about{height:360px;background:linear-gradient(120deg,var(--cream) 0%,#fff5f2 100%)}
.about .sec-title{position:absolute;left:0;top:68px;width:470px}
.about-text{position:absolute;left:0;top:154px;width:350px;font-size:12px;line-height:19px;color:#403a3d}
.about .btn{position:absolute;left:0;top:254px;height:40px;padding:0 23px;font-size:12px}
.features{position:absolute;right:0;top:56px;width:373px;display:flex;flex-direction:column;gap:15px}
.feature{height:73px;background:#fff;border-radius:10px;box-shadow:0 3px 14px rgba(160,40,70,.06);display:flex;align-items:center;gap:16px;padding:0 16px}
.feature .ic{width:38px;height:38px;border-radius:50%;background:var(--magenta-soft);color:var(--magenta);display:flex;align-items:center;justify-content:center}
.feature b{display:block;font-family:'Cormorant Garamond',serif;font-weight:600;font-size:16px}
.feature span{font-size:10px;color:var(--muted)}

/* services */
.services{height:496px;text-align:center}
.eyebrow{font-size:10px;font-weight:700;letter-spacing:1.2px;color:var(--gold)}
.services .eyebrow{position:absolute;left:0;right:0;top:72px}
.services .sec-title{position:absolute;left:0;right:0;top:90px}
.services .rule{left:488px;top:140px}
.svc-grid{position:absolute;left:0;top:183px;display:flex;gap:22px;text-align:left}
.svc-card{width:328px;height:250px;background:#fff;border-radius:14px;box-shadow:0 4px 18px rgba(160,40,70,.07);padding:26px 26px}
.svc-card .ic{width:46px;height:46px;border-radius:12px;background:var(--magenta-soft);color:var(--magenta);display:flex;align-items:center;justify-content:center}
.svc-card .ic svg{width:20px;height:20px}
.svc-card h3{font-family:'Cormorant Garamond',serif;font-weight:600;font-size:21px;margin-top:22px}
.svc-card p{font-size:12px;line-height:19px;color:var(--muted);margin-top:12px}
.more{display:flex;align-items:center;gap:5px;margin-top:22px;font-size:12px;font-weight:600;color:var(--magenta)}

/* gallery */
.gallery{height:437px;background:linear-gradient(180deg,var(--cream) 0%,#fffdf8 100%)}
.gallery .eyebrow{position:absolute;left:0;top:100px}
.gallery .sec-title{position:absolute;left:0;top:122px;width:250px;font-size:26px;line-height:30px;white-space:nowrap}
.gallery-text{position:absolute;left:0;top:198px;width:245px;font-size:12px;line-height:19px;color:#5b5458}
.gallery .btn{position:absolute;left:0;top:312px;height:36px;padding:0 20px;font-size:12px}
.tiles{position:absolute;left:262px;top:70px;display:flex;gap:20px}
.tile{position:relative;width:242px;height:302px;border-radius:16px;box-shadow:0 8px 22px rgba(0,0,0,.12)}
.tile-shop{background:linear-gradient(160deg,#1f2d4a 0%,#3a3f55 50%,#6b4a2a 100%)}
.tile-flowers{background:linear-gradient(160deg,#3f4b5f 0%,#7b5a7a 40%,#d9b8a6 70%,#2f3b2f 100%)}
.tile-roses{background:linear-gradient(160deg,#1f3a34 0%,#a3162a 45%,#1c2e2a 100%)}
.tile-tag{position:absolute;left:16px;bottom:14px;background:var(--magenta);color:#fff;font-size:10px;font-weight:600;padding:6px 12px;border-radius:14px}

/* cta */
.cta{height:360px}
.cta-box{position:absolute;left:0;top:56px;width:1028px;height:250px;border-radius:26px;background:linear-gradient(120deg,#fde3ea 0%,#fff3f1 60%,#fff8ee 100%);border:1px solid #f6dde3}
.cta-box h2{position:absolute;left:48px;top:48px;font-family:'Cormorant Garamond',serif;font-weight:600;font-size:31px}
.cta-box p{position:absolute;left:48px;top:102px;width:430px;font-size:13px;line-height:22px;color:#3d3639}
.cta-quote{position:absolute;left:48px;top:190px;font-size:15px;font-style:italic;color:var(--magenta)}
.cta-actions{position:absolute;right:48px;top:102px;display:flex;gap:14px}
.cta-actions .btn{height:48px;padding:0 28px;font-size:14px}
.cta-actions .btn-chat{background:#fff}

/* footer */
.site-footer{height:337px;background:#f7f7f8}
.f-brand{position:absolute;left:0;top:56px}
.f-brand .brand-kicker{letter-spacing:1px}
.f-text{position:absolute;left:0;top:120px;width:260px;font-size:12px;line-height:19px;color:#5b5458}
.f-chat{position:absolute;left:0;top:200px;height:34px;padding:0 18px;font-size:12px;background:#1fae6c;color:#fff}
.f-col{position:absolute;width:180px;font-size:12px;line-height:19px;color:#5b5458}
.f-col h4{font-size:12px;font-weight:700;color:var(--ink);margin-bottom:12px}
.f-col .tel{color:var(--magenta);margin-top:4px;font-weight:500}
.f-col li{list-style:none;margin-bottom:10px}
.bottom-bar{height:44px;background:var(--magenta-dark);color:#fff;font-size:12px;font-weight:600}
.bottom-bar .wrap{display:flex;justify-content:space-between;align-items:center}
.bottom-bar span{display:flex;align-items:center;gap:6px}
.bottom-bar .copy{font-weight:500}
</style>
</head>
<body>
<svg width="0" height="0" style="position:absolute">
  <defs>
    <symbol id="phone" viewBox="0 0 24 24"><path d="M22 16.9v3a2 2 0 0 1-2.2 2 19.8 19.8 0 0 1-8.6-3.1 19.5 19.5 0 0 1-6-6A19.8 19.8 0 0 1 2.1 4.2 2 2 0 0 1 4.1 2h3a2 2 0 0 1 2 1.7c.1 1 .4 1.9.7 2.8a2 2 0 0 1-.5 2.1L8 9.9a16 16 0 0 0 6 6l1.3-1.3a2 2 0 0 1 2.1-.4c.9.3 1.8.6 2.8.7a2 2 0 0 1 1.7 2z"/></symbol>
    <symbol id="pin" viewBox="0 0 24 24"><path d="M20 10c0 6-8 12-8 12s-8-6-8-12a8 8 0 0 1 16 0z"/><circle cx="12" cy="10" r="3"/></symbol>
    <symbol id="chat" viewBox="0 0 24 24"><path d="M4 5h16v11H9l-5 4z"/></symbol>
    <symbol id="heart" viewBox="0 0 24 24"><path d="M20.8 4.6a5.5 5.5 0 0 0-7.8 0L12 5.7l-1-1.1a5.5 5.5 0 0 0-7.8 7.8L12 21l8.8-8.6a5.5 5.5 0 0 0 0-7.8z"/></symbol>
    <symbol id="house" viewBox="0 0 24 24"><path d="M3 21V10l9-7 9 7v11z"/><path d="M9 21v-6h6v6"/><path d="M12 6v5M10 8h4"/></symbol>
    <symbol id="clock" viewBox="0 0 24 24"><circle cx="12" cy="12" r="9"/><path d="M12 7v5l3 2"/></symbol>
    <symbol id="doc" viewBox="0 0 24 24"><path d="M14 3H6v18h12V7z"/><path d="M14 3v4h4M9 13h6M9 17h6"/></symbol>
    <symbol id="cal" viewBox="0 0 24 24"><rect x="3" y="5" width="18" height="16" rx="2"/><path d="M3 10h18M8 3v4M16 3v4"/></symbol>
    <symbol id="flame" viewBox="0 0 24 24"><path d="M12 3c1 4 6 6 6 11a6 6 0 0 1-12 0c0-3 2-4 2-7 2 1 3 3 3 5 1-2 1-6 1-9z"/></symbol>
    <symbol id="hands" viewBox="0 0 24 24"><path d="M3 15l5-5 4 3 4-4 5 5-5 5H9z"/><path d="M12 13l3 3"/></symbol>
    <symbol id="arrow" viewBox="0 0 24 24"><path d="M5 12h14M13 6l6 6-6 6"/></symbol>
  </defs>
</svg>

<header class="site-header">
  <div class="wrap">
    <div class="brand">
      <div class="brand-dot"></div>
      <div>
        <div class="brand-kicker">Bestattung</div>
        <div class="brand-name">Helga Rothmaier</div>
        <div class="brand-tag">Einfühlsame Begleitung im Trauerfall</div>
      </div>
    </div>
    <nav class="nav"><span>Leistungen</span><span>Bestattungsarten</span><span>Galerie</span><span>Unternehmen</span><span>Standorte</span><span>Kontakt</span></nav>
    <div class="header-actions">
      <a class="btn btn-magenta"><svg class="i"><use href="#phone"/></svg>Jetzt anrufen</a>
      <a class="btn btn-outline"><svg class="i"><use href="#chat"/></svg>Messenger</a>
    </div>
  </div>
</header>

<section class="hero">
  <div class="wrap">
    <div class="badge"><svg class="i" style="width:11px;height:11px"><use href="#heart"/></svg>Schnelle Hilfe im Trauerfall</div>
    <h1>Bestattung Helga Rothmaier<br>– wir begleiten Sie<br><span class="accent">einfühlsam</span> und zuverlässig</h1>
    <p class="hero-lead">In schweren Momenten stehen wir Angehörigen mit klarer Beratung, persönlicher Betreuung und schneller Hilfe zur Seite.</p>
    <div class="hero-actions">
      <a class="btn btn-magenta"><svg class="i"><use href="#phone"/></svg>Sofort anrufen</a>
      <a class="btn btn-gold"><svg class="i"><use href="#pin"/></svg>Standorte</a>
      <a class="btn btn-chat"><svg class="i"><use href="#chat"/></svg>Messenger</a>
    </div>
    <div class="hero-photo" role="img" aria-label="Foto: Sonnenaufgang über einem Wolkenmeer"></div>
    <div class="reach-card">
      <div class="reach-top">
        <div class="reach-ic"><svg class="i"><use href="#phone"/></svg></div>
        <div><b>Telefonisch erreichbar</b><span>Wir sind gerne für Sie da – jederzeit.</span></div>
      </div>
      <div class="reach-places">
        <span><svg class="i"><use href="#pin"/></svg>Frankenberg</span>
        <span><svg class="i"><use href="#pin"/></svg>Hainichen</span>
        <span><svg class="i"><use href="#pin"/></svg>Flöha</span>
        <span><svg class="i"><use href="#pin"/></svg>Roßwein</span>
        <span><svg class="i"><use href="#pin"/></svg>Chemnitz</span>
      </div>
    </div>
  </div>
</section>

<section class="locations">
  <div class="wrap">
    <h2 class="sec-title">Wir sind an mehreren <span class="accent">Standorten</span> für Sie da</h2>
    <div class="rule" style="left:0;top:101px"></div>
    <div class="info-note">
      <div class="ic"><svg class="i"><use href="#chat"/></svg></div>
      <div>Alle Telefonnummern sind direkt klickbar.<br>Für eine schnelle Abstimmung erreichen Sie uns auch per <b>Messenger</b>.</div>
    </div>
    <div class="loc-grid">
      <div class="loc-card"><div class="loc-ic"><svg class="i"><use href="#house"/></svg></div><h3>Frankenberg</h3><p>Lindenweg 8<br>09669 Frankenberg</p><a class="btn btn-magenta"><svg class="i"><use href="#phone"/></svg>037206 / 4810</a><div class="route"><svg class="i"><use href="#pin"/></svg>Route anzeigen</div></div>
      <div class="loc-card"><div class="loc-ic"><svg class="i"><use href="#house"/></svg></div><h3>Hainichen</h3><p>Gartenstraße 17<br>09661 Hainichen</p><a class="btn btn-magenta"><svg class="i"><use href="#phone"/></svg>037207 / 5392</a><div class="route"><svg class="i"><use href="#pin"/></svg>Route anzeigen</div></div>
      <div class="loc-card"><div class="loc-ic"><svg class="i"><use href="#house"/></svg></div><h3>Flöha</h3><p>Parkallee 24<br>09557 Flöha</p><a class="btn btn-magenta"><svg class="i"><use href="#phone"/></svg>03726 / 481205</a><div class="route"><svg class="i"><use href="#pin"/></svg>Route anzeigen</div></div>
      <div class="loc-card"><div class="loc-ic"><svg class="i"><use href="#house"/></svg></div><h3>Roßwein</h3><p>Mühlenweg 5<br>04741 Roßwein</p><a class="btn btn-magenta"><svg class="i"><use href="#phone"/></svg>034322 / 58204</a><div class="route"><svg class="i"><use href="#pin"/></svg>Route anzeigen</div></div>
      <div class="loc-card"><div class="loc-ic"><svg class="i"><use href="#house"/></svg></div><h3>Chemnitz</h3><p>Ahornstraße 63<br>09117 Chemnitz</p><a class="btn btn-magenta"><svg class="i"><use href="#phone"/></svg>0371 / 9402718</a><div class="route"><svg class="i"><use href="#pin"/></svg>Route anzeigen</div></div>
    </div>
  </div>
</section>

<section class="about">
  <div class="wrap">
    <h2 class="sec-title">Einfühlsame Unterstützung seit <span class="accent">über 30 Jahren</span></h2>
    <p class="about-text">Wir beraten Sie gern zu allen Entscheidungen, die in einem Trauerfall getroffen werden müssen. Von der Erledigung der Formalitäten über die Bestattungsarten bis zur Gestaltung der Trauerfeier begleiten wir Sie persönlich und zuverlässig.</p>
    <a class="btn btn-gold">Mehr über uns</a>
    <div class="features">
      <div class="feature"><div class="ic"><svg class="i"><use href="#clock"/></svg></div><div><b>Über 30 Jahre Erfahrung</b><span>Gelebte Tradition und Fachwissen.</span></div></div>
      <div class="feature"><div class="ic"><svg class="i"><use href="#heart"/></svg></div><div><b>Persönliche Betreuung</b><span>Einfühlsam und individuell an Ihrer Seite.</span></div></div>
      <div class="feature"><div class="ic"><svg class="i"><use href="#doc"/></svg></div><div><b>Hilfe bei Formalitäten</b><span>Umfassende Entlastung für Angehörige.</span></div></div>
    </div>
  </div>
</section>

<section class="services">
  <div class="wrap">
    <div class="eyebrow">WIR ENTLASTEN SIE</div>
    <h2 class="sec-title">Unsere Leistungen</h2>
    <div class="rule"></div>
    <div class="svc-grid">
      <div class="svc-card"><div class="ic"><svg class="i"><use href="#cal"/></svg></div><h3>Planung</h3><p>Kommt es zu einem Todesfall in der Familie, unterstützen wir Sie bei Planung, Organisation und allen notwendigen Formalitäten.</p><div class="more">Mehr erfahren <svg class="i" style="width:12px;height:12px"><use href="#arrow"/></svg></div></div>
      <div class="svc-card"><div class="ic"><svg class="i"><use href="#flame"/></svg></div><h3>Bestattungsarten</h3><p>Wir beraten Sie zu Erd-, Feuer-, Urnen- und Seebestattungen und finden gemeinsam eine passende Form des Abschieds.</p><div class="more">Mehr erfahren <svg class="i" style="width:12px;height:12px"><use href="#arrow"/></svg></div></div>
      <div class="svc-card"><div class="ic"><svg class="i"><use href="#hands"/></svg></div><h3>Betreuung</h3><p>Wir begleiten Sie persönlich, beantworten Ihre Fragen und unterstützen Sie Schritt für Schritt in dieser schweren Zeit.</p><div class="more">Mehr erfahren <svg class="i" style="width:12px;height:12px"><use href="#arrow"/></svg></div></div>
    </div>
  </div>
</section>

<section class="gallery">
  <div class="wrap">
    <div class="eyebrow">IMPRESSIONEN</div>
    <h2 class="sec-title">Ein würdevoller Rahmen<br>für den Abschied</h2>
    <p class="gallery-text">Liebevolle Details, individuelle Gestaltung und eine Atmosphäre, die den Persönlichkeiten des Menschen Raum gibt, machen eine Trauerfeier spürbar persönlich.</p>
    <a class="btn btn-magenta">Zur Galerie</a>
    <div class="tiles">
      <div class="tile tile-shop" role="img" aria-label="Foto: Schaufenster einer Ausstellung am Abend"><span class="tile-tag">Särge und Sarggestecke</span></div>
      <div class="tile tile-flowers" role="img" aria-label="Foto: Blumenstrauß mit Rosen und Trockenblumen"><span class="tile-tag">Blumengestecke</span></div>
      <div class="tile tile-roses" role="img" aria-label="Foto: rote Rosen"><span class="tile-tag">Urnen und Gestecke</span></div>
    </div>
  </div>
</section>

<section class="cta">
  <div class="wrap">
    <div class="cta-box">
      <h2>Sie brauchen jetzt Unterstützung?</h2>
      <p>Rufen Sie uns direkt an oder schreiben Sie uns per Messenger. Wir nehmen uns Zeit, erklären alle Schritte verständlich und sind an allen Standorten für Sie erreichbar.</p>
      <div class="cta-quote">"Wir sind jederzeit für Sie erreichbar."</div>
      <div class="cta-actions">
        <a class="btn btn-magenta"><svg class="i"><use href="#phone"/></svg>037206 / 4810</a>
        <a class="btn btn-chat"><svg class="i"><use href="#chat"/></svg>Messenger</a>
      </div>
    </div>
  </div>
</section>

<footer class="site-footer">
  <div class="wrap">
    <div class="brand f-brand">
      <div class="brand-dot"></div>
      <div>
        <div class="brand-kicker">BESTATTUNG</div>
        <div class="brand-name">Helga Rothmaier</div>
      </div>
    </div>
    <p class="f-text">Einfühlsame Begleitung im Trauerfall. Wir sind im Raum Frankenberg, Hainichen, Flöha, Roßwein und Chemnitz für Sie da.</p>
    <a class="btn f-chat"><svg class="i"><use href="#chat"/></svg>Messenger Kontakt</a>
    <div class="f-col" style="left:424px;top:58px"><h4>Frankenberg</h4>Lindenweg 8<br>09669 Frankenberg<div class="tel">037206 / 4810</div></div>
    <div class="f-col" style="left:636px;top:58px"><h4>Hainichen</h4>Gartenstraße 17<br>09661 Hainichen<div class="tel">037207 / 5392</div></div>
    <div class="f-col" style="left:848px;top:58px"><h4>Flöha</h4>Parkallee 24<br>09557 Flöha<div class="tel">03726 / 481205</div></div>
    <div class="f-col" style="left:424px;top:177px"><h4>Roßwein</h4>Mühlenweg 5<br>04741 Roßwein<div class="tel">034322 / 58204</div></div>
    <div class="f-col" style="left:636px;top:177px"><h4>Chemnitz</h4>Ahornstraße 63<br>09117 Chemnitz<div class="tel">0371 / 9402718</div></div>
    <div class="f-col" style="left:848px;top:177px"><h4>Informationen</h4><ul><li>Impressum</li><li>Datenschutz</li><li>Kontakt</li></ul></div>
  </div>
</footer>
<div class="bottom-bar">
  <div class="wrap">
    <span><svg class="i" style="width:12px;height:12px"><use href="#heart"/></svg>Einfühlsam. Persönlich. Verlässlich.</span>
    <span class="copy">© 2026 Bestattung Helga Rothmaier. Alle Rechte vorbehalten.</span>
  </div>
</div>
</body>
</html>
```